Property Report

8 page document, similar theme to our website (www.harbourandmeadows.com) and previous brochure (provided). All content provided. We want a professional looking document. We need ASAP. Thanks!

Industry/Entity Type

Property

Font styles to use
Serif
Sans Serif

Colors
ffc214
ffcf3e
fee18a
fff3d1

Requirements
Must have
• Page 1: Cover
Page 2: Content
Page 3: About Us
Page 4: Site Description
Page 5: Scheme
Page 6: Analysis
Page 7: Conclusion
Page 8: Contact Details

```html
<!DOCTYPE html>
<html lang="en">
<head>
<meta charset="utf-8">
<title>Harbour &amp; Meadows – Site Report</title>
<link href="https://fonts.googleapis.com/css2?family=Montserrat:wght@400;600;700;800&family=Open+Sans:wght@400;600&display=swap" rel="stylesheet">
<style>
:root{
  --yellow:#ffc214;
  --yellow-2:#ffcf3e;
  --yellow-3:#fee18a;
  --cream:#fff3d1;
  --charcoal:#4e5357;
  --slate:#6b7075;
  --placeholder:#d9d9d9;
  --placeholder-text:#9a9a9a;
  --ink:#3a3d40;
  --paper:#ffffff;
  --canvas:#eceded;
}
*{box-sizing:border-box;margin:0;padding:0}
html,body{width:878px;height:1200px;overflow:hidden;background:var(--canvas)}
body{font-family:'Open Sans',sans-serif;color:var(--ink);position:relative}
.spread{position:absolute;inset:0;display:grid;grid-template-columns:repeat(3,256px);grid-template-rows:repeat(3,362px);gap:24px 22px;padding:34px 33px}
.page{position:relative;background:var(--paper);overflow:hidden;box-shadow:0 1px 4px rgba(0,0,0,.18)}
.page.dark{background:var(--charcoal)}
.photo{position:absolute;background:linear-gradient(160deg,#8d9296 0%,#5e6367 55%,#3f4347 100%)}
.photo.site{background:linear-gradient(175deg,#a9c2da 0%,#b7c3cc 40%,#8a7a6a 70%,#6f6458 100%)}
.placeholder{position:absolute;background:var(--placeholder);display:flex;align-items:center;justify-content:center;font-family:'Montserrat',sans-serif;font-size:8px;color:var(--placeholder-text)}
.brand-name{position:absolute;font-family:'Montserrat',sans-serif;font-weight:700;color:#fff;white-space:nowrap;display:flex;align-items:center;gap:5px;line-height:1}
.brand-name .square{width:7px;height:7px;background:var(--yellow);flex:none}
.brand-box{position:absolute;left:0;top:0;width:104px;height:44px;background:var(--charcoal)}
.frame{position:absolute;border:2px solid var(--yellow)}
.heading{font-family:'Montserrat',sans-serif;font-weight:700;color:var(--ink);font-size:13px}
.rule{width:34px;height:2px;background:var(--yellow);margin-top:4px}
.body-text{font-size:4.2px;line-height:1.55;color:#555}
.folio{position:absolute;bottom:8px;right:12px;font-size:5px;color:#888}

/* cover */
.cover-banner{position:absolute;left:0;top:218px;width:180px;height:22px;background:var(--yellow);font-family:'Montserrat',sans-serif;font-weight:800;font-size:12px;color:#fff;padding:4px 12px;letter-spacing:.5px}
.cover-address{position:absolute;left:12px;top:248px;font-family:'Montserrat',sans-serif;font-size:6px;font-weight:600;color:var(--ink)}
.cover-sub{position:absolute;left:12px;top:262px;font-size:4.2px;color:#777}
.cover-foot{position:absolute;left:0;right:0;bottom:0;height:60px;background:var(--charcoal)}

/* contents & about */
.panel{position:absolute;background:var(--cream);padding:14px 14px}
.contents-list{list-style:none;margin-top:10px}
.contents-list li{display:flex;align-items:center;gap:6px;font-size:5.5px;color:var(--ink);margin-bottom:7px;font-family:'Montserrat',sans-serif}
.contents-list li::before{content:"";width:7px;height:7px;background:var(--yellow)}

/* inner page header */
.page-head{position:absolute;left:14px;top:14px}
.columns{position:absolute;left:14px;right:14px;top:48px;display:grid;grid-template-columns:1fr 1fr;gap:10px}

/* case studies */
.case{position:absolute;left:128px;width:116px}
.case h4{font-family:'Montserrat',sans-serif;font-size:5px;font-weight:700;color:#c99400;margin-bottom:2px}

/* analysis table */
.analysis-sub{font-family:'Montserrat',sans-serif;font-size:5px;font-weight:600;margin-top:6px;color:var(--ink)}
.data{position:absolute;left:14px;right:14px;top:60px;border-collapse:collapse;font-size:3.6px;width:228px}
.data th{background:var(--yellow);color:#fff;height:10px;font-weight:600}
.data td{height:9.5px;border-bottom:1px solid #e5e5e5;color:#777;text-align:center}
.data td:first-child{background:var(--slate);color:#fff}
.data tr:nth-child(even) td:not(:first-child){background:#fafafa}

/* conclusion */
.conclusion-title{position:absolute;left:0;right:0;top:34px;text-align:center;font-family:'Montserrat',sans-serif;font-weight:700;color:#fff;font-size:11px}
.conclusion-title .rule{margin:4px auto 0}
.conclusion-panel{position:absolute;left:20px;right:20px;top:88px;bottom:24px;background:var(--cream);padding:14px 16px;text-align:center}
.conclusion-panel h5{font-family:'Montserrat',sans-serif;font-size:5.5px;font-weight:700;margin:8px 0 3px}
.benefit-grid{display:grid;grid-template-columns:1fr 1fr;gap:8px;margin-top:6px}

/* back cover */
.back-contact{position:absolute;left:14px;bottom:14px;font-size:4.5px;color:#fff;line-height:1.6}
.back-contact strong{font-family:'Montserrat',sans-serif;font-size:5px}
</style>
</head>
<body>
<main class="spread">

  <!-- Cover -->
  <section class="page cover">
    <div class="photo site" role="img" aria-label="Photograph of the building site with scaffolding" style="left:0;top:0;width:256px;height:218px"></div>
    <div class="brand-box"></div>
    <div class="brand-name" style="left:10px;top:18px;font-size:8px">Harbour &amp; Meadows<span class="square"></span></div>
    <div class="cover-banner">SITE REPORT</div>
    <p class="cover-address">14 Wharfside Lane, Eastmoor, EM4 2QH</p>
    <p class="cover-sub">Prepared by Harbour &amp; Meadows Commercial · Spring Edition</p>
    <div class="cover-foot"></div>
  </section>

  <!-- Contents -->
  <section class="page dark">
    <div class="photo" role="img" aria-label="Muted photograph of a city skyline" style="inset:0;opacity:.85"></div>
    <div class="brand-name" style="left:16px;top:18px;font-size:8px">Harbour &amp; Meadows<span class="square"></span></div>
    <div class="frame" style="left:40px;top:64px;width:176px;height:230px"></div>
    <div class="panel" style="left:56px;top:80px;width:146px;height:200px">
      <h2 class="heading">Contents</h2>
      <ul class="contents-list">
        <li>About Us</li><li>Site Description</li><li>Scheme</li>
        <li>Case Studies</li><li>Analysis</li><li>Conclusion</li><li>Contact Details</li>
      </ul>
    </div>
  </section>

  <!-- About Us -->
  <section class="page dark">
    <div class="photo" role="img" aria-label="Muted photograph of a city skyline at dusk" style="inset:0;opacity:.85"></div>
    <div class="brand-name" style="left:14px;top:18px;font-size:7px">Harbour &amp; Meadows</div>
    <div class="panel" style="left:118px;top:0;width:138px;height:362px;padding-top:22px">
      <h2 class="heading">About Us</h2>
      <div class="rule"></div>
      <p class="body-text" style="margin-top:10px">We are an independent property consultancy offering sales, lettings and investment advice across the region. Our team combines local knowledge with a practical, hands-on approach to every instruction we take on.</p>
      <p class="body-text" style="margin-top:8px">From single units to large mixed-use schemes, we guide clients through each stage of acquisition, planning and disposal with clear and honest advice.</p>
      <p class="body-text" style="margin-top:8px">Our commercial division works closely with developers, landowners and occupiers to secure the best outcome for every site.</p>
    </div>
  </section>

  <!-- Site Description -->
  <section class="page">
    <div class="page-head"><h2 class="heading">Site Description</h2><div class="rule"></div></div>
    <div class="columns">
      <p class="body-text">The site extends to approximately 0.4 acres and sits on the corner of two busy streets close to the town centre, rail station and local amenities.</p>
      <p class="body-text">The existing structure is a two storey brick building with yard space to the rear and pedestrian access from the main frontage.</p>
    </div>
    <div class="placeholder" role="img" aria-label="Photograph of the site" style="left:14px;right:14px;top:112px;height:190px">Image</div>
    <span class="folio">4</span>
  </section>

  <!-- Scheme -->
  <section class="page">
    <div class="page-head"><h2 class="heading">Scheme</h2><div class="rule"></div></div>
    <p class="body-text" style="position:absolute;left:110px;top:16px;width:132px">The proposed scheme delivers new homes with ground floor commercial space and landscaped shared courtyards.</p>
    <div class="placeholder" role="img" aria-label="Scheme drawing" style="left:14px;top:58px;width:92px;height:110px">Image</div>
    <div class="placeholder" role="img" aria-label="Scheme elevation" style="left:112px;top:58px;width:130px;height:110px">Image</div>
    <div class="placeholder" role="img" aria-label="Scheme visual" style="left:14px;top:176px;width:228px;height:150px">Image</div>
    <span class="folio">5</span>
  </section>

  <!-- Case Studies -->
  <section class="page">
    <div class="page-head"><h2 class="heading">Case Studies</h2><div class="rule"></div>
      <p class="body-text" style="margin-top:4px">Comparable</p></div>
    <div class="placeholder" role="img" aria-label="Case study photograph" style="left:14px;top:62px;width:104px;height:84px">Image</div>
    <div class="placeholder" role="img" aria-label="Case study photograph" style="left:14px;top:152px;width:104px;height:84px">Image</div>
    <div class="placeholder" role="img" aria-label="Case study photograph" style="left:14px;top:242px;width:104px;height:84px">Image</div>
    <div class="case" style="top:66px"><h4>Riverside Housing Scheme, Mill Road, Eastmoor EM2 5TL</h4><p class="body-text">Twenty four apartments delivered on a former depot site, fully let within six months.</p></div>
    <div class="case" style="top:156px"><h4>Canal Quarter, Lock Street, Eastmoor EM1 8RB</h4><p class="body-text">Mixed-use scheme with retail at ground level and homes above, completed last year.</p></div>
    <div class="case" style="top:246px"><h4>Station Gardens, Grove Road, Eastmoor EM3 1JD</h4><p class="body-text">Conversion of an office block into family homes with private gardens and parking.</p></div>
    <span class="folio">6</span>
  </section>

  <!-- Analysis -->
  <section class="page">
    <div class="page-head"><h2 class="heading">Analysis</h2><div class="rule"></div>
      <p class="analysis-sub">Comparable Transaction Evidence</p></div>
    <table class="data">
      <thead><tr><th></th><th>Address</th><th>Type</th><th>Size</th><th>Price</th><th>Date</th></tr></thead>
      <tbody>
        <tr><td>Unit 1</td><td>Mill Road</td><td>Flat</td><td>62 sqm</td><td>£195k</td><td>Jan</td></tr>
        <tr><td>Unit 2</td><td>Lock Street</td><td>Flat</td><td>71 sqm</td><td>£210k</td><td>Feb</td></tr>
        <tr><td>Unit 3</td><td>Grove Road</td><td>House</td><td>94 sqm</td><td>£285k</td><td>Mar</td></tr>
        <tr><td>Unit 4</td><td>Quay Lane</td><td>Flat</td><td>58 sqm</td><td>£180k</td><td>Apr</td></tr>
        <tr><td>Unit 5</td><td>Park Row</td><td>House</td><td>102 sqm</td><td>£310k</td><td>May</td></tr>
        <tr><td>Unit 6</td><td>Mill Road</td><td>Flat</td><td>66 sqm</td><td>£199k</td><td>Jun</td></tr>
        <tr><td>Unit 7</td><td>High Street</td><td>Retail</td><td>120 sqm</td><td>£340k</td><td>Jul</td></tr>
      </tbody>
    </table>
    <span class="folio">7</span>
  </section>

  <!-- Conclusion -->
  <section class="page">
    <div class="photo" role="img" aria-label="Muted photograph of an office interior" style="left:0;top:0;width:256px;height:150px"></div>
    <div class="conclusion-title">Conclusion<div class="rule"></div></div>
    <div class="conclusion-panel">
      <p class="body-text">The site offers a strong opportunity for residential led redevelopment, supported by local demand and recent comparable sales in the immediate area.</p>
      <h5>Benefits</h5>
      <p class="body-text">Central location, good transport links and a clear planning route.</p>
      <div class="benefit-grid">
        <div><h5>Private Sale</h5><p class="body-text">Discreet marketing to a selected group of buyers.</p></div>
        <div><h5>Alternative Use</h5><p class="body-text">Scope for commercial or mixed-use options.</p></div>
      </div>
    </div>
  </section>

  <!-- Contact Details -->
  <section class="page dark">
    <div class="photo" role="img" aria-label="Dark photograph of a city skyline" style="inset:0;opacity:.9"></div>
    <div class="frame" style="left:118px;top:168px;width:110px;height:90px"></div>
    <div class="brand-name" style="left:40px;top:206px;font-size:16px">Harbour &amp; Meadows</div>
    <div class="back-contact"><strong>Harbour &amp; Meadows Commercial</strong><br>www.harbourandmeadows.com</div>
  </section>

</main>
</body>
</html>
```